Supermarket Business Card Design
Pellman's Supermarket
Use standard fonts
Tobias Pellman
President
478 Linden Ave.
Ashford, VT 05761
tpellman@pellmansupermarket.com
This is the logo I would like in the business card
Here is the logo in AI format but I want the logo on the left to be used

```html
<!DOCTYPE html>
<html lang="en">
<head>
<meta charset="utf-8">
<title>Pellman's Supermarket – Business Card</title>
<link href="https://fonts.googleapis.com/css2?family=Marcellus+SC&display=swap" rel="stylesheet">
<style>
  :root {
    --backdrop: #ecebe8;
    --card: #ffffff;
    --brand-red: #c8202a;
    --ink-grey: #7a7a7a;
    --shadow: rgba(0,0,0,0.14);
  }
  * { margin: 0; padding: 0; box-sizing: border-box; }
  html, body {
    width: 1200px; height: 629px; overflow: hidden;
    background: var(--backdrop);
    font-family: "Marcellus SC", Georgia, serif;
  }
  .stage {
    position: relative; width: 1200px; height: 629px;
    display: flex; gap: 40px; justify-content: center; align-items: center;
  }
  .card {
    position: relative; width: 520px; height: 298px;
    background: var(--card);
    box-shadow: 0 6px 18px var(--shadow);
  }
  .brand { display: flex; align-items: center; gap: 10px; }
  .brand-dot { border-radius: 50%; background: var(--brand-red); flex: none; }
  .brand-name { color: var(--brand-red); line-height: 1; white-space: nowrap; }

  .card-front { display: flex; align-items: center; justify-content: center; }
  .card-front .brand-dot { width: 54px; height: 54px; }
  .card-front .brand-name { font-size: 30px; }

  .card-back .brand { position: absolute; left: 34px; top: 34px; }
  .card-back .brand-dot { width: 34px; height: 34px; }
  .card-back .brand-name { font-size: 19px; }

  .holder { position: absolute; right: 40px; top: 108px; text-align: right; }
  .holder-name { color: var(--brand-red); font-size: 17px; letter-spacing: 0.5px; }
  .holder-title { color: var(--ink-grey); font-size: 11px; margin-top: 3px; }

  .contacts {
    position: absolute; right: 40px; top: 166px;
    list-style: none; display: flex; flex-direction: column; gap: 7px;
  }
  .contact {
    display: flex; align-items: center; justify-content: flex-end; gap: 8px;
    font-size: 10px; line-height: 14px; color: var(--ink-grey); letter-spacing: 0.3px;
    white-space: nowrap;
  }
  .contact-icon {
    flex: none; width: 14px; height: 14px; border-radius: 50%;
    background: var(--brand-red);
    display: flex; align-items: center; justify-content: center;
  }
  .contact-icon svg { width: 8px; height: 8px; }

  .address {
    position: absolute; left: 34px; bottom: 26px;
    font-size: 10px; color: var(--ink-grey); letter-spacing: 0.4px; line-height: 1.5;
  }
</style>
</head>
<body>
<main class="stage">
  <section class="card card-front" aria-label="Card front">
    <div class="brand">
      <span class="brand-dot"></span>
      <span class="brand-name">Pellman's Supermarket</span>
    </div>
  </section>

  <section class="card card-back" aria-label="Card back">
    <div class="brand">
      <span class="brand-dot"></span>
      <span class="brand-name">Pellman's Supermarket</span>
    </div>

    <div class="holder">
      <p class="holder-name">Tobias Pellman</p>
      <p class="holder-title">President</p>
    </div>

    <ul class="contacts">
      <li class="contact">
        <span class="contact-icon">
          <svg viewBox="0 0 10 10"><path d="M2 1 L4 1 L4.6 3 L3.5 4 Q4.5 6 6 6.5 L7 5.4 L9 6 L9 8 Q5 9.5 1 4 Z" fill="#fff"/></svg>
        </span>
        <span>(802) 555-0142</span>
      </li>
      <li class="contact">
        <span class="contact-icon">
          <svg viewBox="0 0 10 10"><rect x="1" y="2.5" width="8" height="5" fill="#fff"/><path d="M1 2.5 L5 5.5 L9 2.5" stroke="#c8202a" stroke-width="0.8" fill="none"/></svg>
        </span>
        <span>tpellman@pellmansupermarket.com</span>
      </li>
      <li class="contact">
        <span class="contact-icon"></span>
        <span>tpellman4472</span>
      </li>
      <li class="contact">
        <span class="contact-icon"></span>
        <span>pellman_s_supermarket</span>
      </li>
    </ul>

    <p class="address">478 Linden Ave.<br>Ashford, VT 05761</p>
  </section>
</main>
</body>
</html>
```